Roofing Company Sales Rep Business Card

Business card for sales rep to canvass and hand out to property owners/managers for free roof inspections and roof replacements.

```html
<!DOCTYPE html>
<html lang="en">
<head>
<meta charset="utf-8">
<title>Ridge Line Roofing – Business Card</title>
<link rel="stylesheet" href="https://fonts.googleapis.com/css2?family=Montserrat:wght@400;500;700&display=swap">
<style>
  :root {
    --page: #ffffff;
    --card-dark: #060606;
    --card-mid: #3a3a3a;
    --accent: #ffc107;
    --ink-light: #ffffff;
    --shadow: rgba(0, 0, 0, 0.35);
  }
  * { margin: 0; padding: 0; box-sizing: border-box; }
  html, body {
    width: 1200px; height: 1000px; overflow: hidden;
    background: var(--page);
    font-family: "Montserrat", Arial, sans-serif;
  }
  .canvas { position: relative; width: 1200px; height: 1000px; }
  .card {
    position: absolute; left: 265px; width: 670px; height: 382px;
    background: linear-gradient(135deg, var(--card-dark) 0%, var(--card-mid) 48%, var(--card-mid) 55%, var(--card-dark) 100%);
    box-shadow: 8px 10px 18px var(--shadow);
    overflow: hidden; color: var(--ink-light);
  }
  .card--front { top: 109px; }
  .card--back { top: 509px; }

  /* Front */
  .brand-circle {
    position: absolute; border-radius: 50%; background: var(--accent);
  }
  .card--front .brand-circle { left: 333px; top: 66px; width: 120px; height: 120px; }
  .front-name {
    position: absolute; left: 0; right: 0; top: 222px; text-align: center;
    font-weight: 700; font-size: 40px; letter-spacing: 1px; color: var(--accent);
  }

  /* Back */
  .back-name {
    position: absolute; left: 41px; top: 40px;
    font-weight: 700; font-size: 38px; letter-spacing: 1px; color: var(--accent);
  }
  .rep { position: absolute; left: 41px; top: 160px; }
  .rep__name { font-weight: 700; font-size: 27px; letter-spacing: 1px; line-height: 1.1; }
  .rep__title { font-weight: 400; font-size: 20px; letter-spacing: 1px; margin-top: 2px; }
  .contacts { position: absolute; left: 41px; top: 270px; list-style: none; }
  .contacts li {
    display: flex; align-items: center; gap: 14px;
    font-size: 19px; font-weight: 500; height: 26px;
  }
  .contacts svg { width: 18px; height: 18px; fill: var(--accent); flex: none; }
  .card--back .brand-circle { left: 522px; top: 206px; width: 120px; height: 120px; }
  .accent-band {
    position: absolute; left: 0; right: 0; bottom: 0; height: 13px; background: var(--accent);
  }
</style>
</head>
<body>
<main class="canvas">
  <section class="card card--front" aria-label="Card front">
    <div class="brand-circle"></div>
    <p class="front-name">RIDGE LINE ROOFING</p>
  </section>

  <section class="card card--back" aria-label="Card back">
    <p class="back-name">RIDGE LINE ROOFING</p>
    <div class="rep">
      <p class="rep__name">DANIEL REYES</p>
      <p class="rep__title">PRESIDENT</p>
    </div>
    <ul class="contacts">
      <li>
        <svg viewBox="0 0 24 24" aria-hidden="true"><path d="M6.6 10.8a15.1 15.1 0 0 0 6.6 6.6l2.2-2.2c.3-.3.7-.4 1-.2 1.1.4 2.3.6 3.6.6.6 0 1 .4 1 1V20c0 .6-.4 1-1 1C10.6 21 3 13.4 3 4c0-.6.4-1 1-1h3.5c.6 0 1 .4 1 1 0 1.3.2 2.5.6 3.6.1.3 0 .7-.2 1z"/></svg>
        (555) 284-7710
      </li>
      <li>
        <svg viewBox="0 0 24 24" aria-hidden="true"><path d="M2 5h20v14H2z M2 5l10 8 10-8" /><path d="M2 5h20L12 12.5z" fill="#2a2a2a"/></svg>
        daniel@ridgelineroofing.com
      </li>
      <li>
        <svg viewBox="0 0 24 24" aria-hidden="true"><path d="M12 2a10 10 0 1 0 0 20 10 10 0 0 0 0-20zm1 2.1c1.3.9 2.3 2.9 2.7 5.4H13zm-2 0v5.4H8.3c.4-2.5 1.4-4.5 2.7-5.4zM4.1 11.5h4a18 18 0 0 0 0 1H4.1zm0 1h0zM11 19.9c-1.3-.9-2.3-2.9-2.7-5.4H11zm2 0v-5.4h2.7c-.4 2.5-1.4 4.5-2.7 5.4zm2.9-8.4a18 18 0 0 1 0 1H13v-1zm-4.9 0v1H8.1a18 18 0 0 1 0-1zm6.9 0h2.9v1h-2.9z"/></svg>
        www.ridgelineroofing.com
      </li>
    </ul>
    <div class="brand-circle"></div>
    <div class="accent-band"></div>
  </section>
</main>
</body>
</html>
```